Corvelle Strategies business card

I need a business card for my new strategic consulting LLC, Corvelle Strategies. We specialize in helping people who care about broadband technology and telecommunications policy, and we're based in Washington DC. I'm looking for a card that says smart, credible, future-facing and signals a high level of expertise. It's DC, so there's clearly a limit to how crazy we can go with this card, but I am looking for a design that reflects a company that is comfortable with technology, policy, and having a little bit fun. I'm uploading my logo below, and I'd like to have it be part of the card design in some fashion.
Target Market(s)
Telecommunications and technology policy professionals
Industry/Entity Type
Technology policy
Contact Information for Business Card
Name of business, my name (Glen Mosswater), email (glen@corvellestrategies-example.com) , phone number (202-555-0148)phone number

```html
<!DOCTYPE html>
<html lang="en">
<head>
<meta charset="utf-8">
<title>Corvelle Strategies — Business Card</title>
<link rel="stylesheet" href="https://fonts.googleapis.com/css2?family=Poppins:wght@400;500;700&family=Arimo:wght@400&display=swap">
<style>
  :root {
    --stage: #8e8e8e;
    --card: #ffffff;
    --brand-blue: #0b549e;
    --sun: #fbb040;
    --ink: #111111;
    --mesh-blue: rgba(74, 144, 217, 0.22);
    --mesh-fade: rgba(74, 144, 217, 0);
  }
  * { margin: 0; padding: 0; box-sizing: border-box; }
  html, body { width: 960px; height: 1200px; overflow: hidden; }
  body { background: var(--stage); position: relative; font-family: "Poppins", sans-serif; }

  .card {
    position: absolute;
    left: 61px;
    width: 838px;
    height: 479px;
    background: var(--card);
    overflow: hidden;
  }
  .card--front { top: 85px; }
  .card--back { top: 620px; }

  .network-mesh {
    position: absolute;
    left: 0;
    bottom: 0;
    background: radial-gradient(ellipse at 20% 80%, var(--mesh-blue) 0%, var(--mesh-fade) 70%);
  }
  .card--front .network-mesh { width: 440px; height: 360px; }
  .card--back .network-mesh { width: 310px; height: 220px; opacity: 0.8; }

  .wordmark {
    position: absolute;
    display: flex;
    align-items: center;
    gap: 12px;
    color: var(--brand-blue);
    font-weight: 700;
    white-space: nowrap;
    letter-spacing: -0.5px;
    line-height: 1.2;
  }
  .wordmark__dot {
    border-radius: 50%;
    background: var(--sun);
    flex: none;
  }
  .card--front .wordmark { left: 0; right: 0; top: 168px; justify-content: center; font-size: 46px; }
  .card--front .wordmark__dot { width: 38px; height: 38px; }
  .card--back .wordmark { left: 86px; top: 88px; font-size: 33px; }
  .card--back .wordmark__dot { width: 28px; height: 28px; }

  .tagline {
    position: absolute;
    left: 0;
    right: 0;
    top: 303px;
    text-align: center;
    font-family: "Arimo", sans-serif;
    font-size: 19px;
    letter-spacing: 2.2px;
    color: var(--brand-blue);
  }

  .front-band {
    position: absolute;
    left: 139px;
    width: 561px;
    bottom: 0;
    height: 14px;
    background: var(--brand-blue);
    border-radius: 12px 12px 0 0;
  }

  .capitol-scene {
    position: absolute;
    left: 421px;
    top: 126px;
    width: 417px;
    height: 339px;
    background: linear-gradient(180deg, rgba(200, 220, 245, 0.15) 0%, rgba(120, 170, 230, 0.35) 100%);
  }

  .holder-name {
    position: absolute;
    left: 86px;
    top: 203px;
    font-size: 35px;
    font-weight: 700;
    color: var(--brand-blue);
    letter-spacing: -0.2px;
    line-height: 1.3;
  }

  .contact-list { position: absolute; left: 86px; top: 262px; list-style: none; }
  .contact-item {
    display: flex;
    align-items: center;
    gap: 10px;
    height: 36px;
    font-size: 21px;
    font-weight: 400;
    color: var(--ink);
    white-space: nowrap;
  }
  .contact-icon { width: 20px; height: 20px; flex: none; }

  .back-band {
    position: absolute;
    left: 0;
    right: 0;
    bottom: 0;
    height: 14px;
    background: var(--brand-blue);
  }
</style>
</head>
<body>

  <section class="card card--front" aria-label="Card front">
    <div class="network-mesh" role="img" aria-label="Faint blue network-of-dots pattern"></div>
    <div class="wordmark"><span class="wordmark__dot"></span>Corvelle Strategies</div>
    <p class="tagline">CLEAR STRATEGY. LASTING INFLUENCE.</p>
    <div class="front-band"></div>
  </section>

  <section class="card card--back" aria-label="Card back">
    <div class="network-mesh" role="img" aria-label="Faint blue network-of-dots pattern"></div>
    <div class="capitol-scene" role="img" aria-label="Blue line illustration of the Capitol building with clouds, trees and birds"></div>
    <div class="wordmark"><span class="wordmark__dot"></span>Corvelle Strategies</div>
    <h1 class="holder-name">Glen Mosswater</h1>
    <ul class="contact-list">
      <li class="contact-item">
        <svg class="contact-icon" viewBox="0 0 24 24" aria-hidden="true">
          <path d="M6.6 10.8a15.2 15.2 0 0 0 6.6 6.6l2.2-2.2a1 1 0 0 1 1-.25 11.4 11.4 0 0 0 3.6.57 1 1 0 0 1 1 1V20a1 1 0 0 1-1 1A17 17 0 0 1 3 4a1 1 0 0 1 1-1h3.5a1 1 0 0 1 1 1c0 1.25.2 2.45.57 3.57a1 1 0 0 1-.25 1z" fill="var(--sun)"/>
          <path d="M14 3a7 7 0 0 1 7 7M14 6.5A3.5 3.5 0 0 1 17.5 10" stroke="var(--sun)" stroke-width="1.8" fill="none" stroke-linecap="round"/>
        </svg>
        <span>202-555-0148</span>
      </li>
      <li class="contact-item">
        <svg class="contact-icon" viewBox="0 0 24 24" aria-hidden="true">
          <rect x="2" y="5" width="20" height="14" rx="1" fill="var(--sun)"/>
          <path d="M2.5 5.5 12 13l9.5-7.5M2.5 18.5l7-6M21.5 18.5l-7-6" stroke="#ffffff" stroke-width="1.4" fill="none"/>
        </svg>
        <span>glen@corvellestrategies-example.com</span>
      </li>
    </ul>
    <div class="back-band"></div>
  </section>

</body>
</html>
```